Bellcrest HVAC Business Card design

Looking for a modern professional two sided design. Showing contact info and services provided. Possibly on a silk card stock.
Using blues or greens or greys and maybe metallic. One color or a mixture of these.
Dorian Vance
dvance@bellcresthvac-example.net
555-318-4702
Air Conditioning
Heating
Heat Pumps / Gas / Oil
Ductless mini splits
Controls
VFD's
Pumps
Gas Fitting/Piping
Service and New install
Residential / Commercial
Industry/Entity Type
Mechanical HVAC
Contact Information for Business Card
Logo, contact info and provided services

```html
<!DOCTYPE html>
<html lang="en">
<head>
<meta charset="utf-8">
<title>Bellcrest HVAC Business Card</title>
<link rel="stylesheet" href="https://fonts.googleapis.com/css2?family=Poppins:wght@400;500;700&display=swap">
<style>
  :root {
    --backdrop: #707076;
    --card: #2e2e30;
    --card-edge: #262628;
    --accent: #5b63b6;
    --silver: #c9c9cc;
    --text: #eeeef0;
    --rule: #55555a;
  }
  * { box-sizing: border-box; margin: 0; padding: 0; }
  html, body {
    width: 1200px; height: 900px; overflow: hidden;
    background: var(--backdrop);
    font-family: "Poppins", sans-serif;
    color: var(--text);
  }
  .canvas { position: relative; width: 1200px; height: 900px; }
  .card {
    position: absolute; left: 230px; width: 740px; height: 410px;
    background: var(--card); border-radius: 22px;
    box-shadow: 0 10px 26px rgba(0,0,0,.35);
    overflow: hidden;
  }
  .card--front { top: 30px; }
  .card--back { top: 460px; }

  /* brand lockup */
  .brand { display: flex; align-items: center; gap: 14px; }
  .brand__dot {
    width: 46px; height: 46px; border-radius: 50%;
    border: 4px solid var(--silver);
  }
  .brand__name {
    font-weight: 700; font-size: 30px; color: var(--silver);
    letter-spacing: 1px; line-height: 1.1;
  }

  /* front */
  .front__ring {
    position: absolute; right: 90px; top: -70px;
    width: 300px; height: 300px; border-radius: 50%;
    border: 6px solid #4a4a4e;
  }
  .front__brand { position: absolute; left: 56px; top: 120px; }
  .front__rule {
    position: absolute; left: 50px; right: 40px; top: 318px;
    height: 1px; background: var(--accent);
  }
  .person { position: absolute; left: 56px; top: 240px; }
  .person__name {
    font-weight: 700; font-size: 36px; color: var(--accent);
    letter-spacing: 1px; line-height: 1;
  }
  .person__role { font-size: 18px; margin-top: 8px; }
  .contact {
    display: flex; align-items: center; gap: 10px;
    font-size: 18px; position: absolute;
  }
  .contact svg { fill: var(--accent); flex: none; }
  .contact--phone { left: 56px; top: 332px; }
  .contact--email { right: 44px; top: 282px; }

  /* back */
  .back__brand { position: absolute; left: 60px; top: 150px; }
  .back__divider {
    position: absolute; left: 372px; top: 50px; width: 1px; height: 250px;
    background: var(--rule);
  }
  .services {
    position: absolute; left: 400px; top: 44px; list-style: none;
    font-size: 18px; line-height: 26.5px;
  }
  .services li { display: flex; align-items: center; gap: 14px; }
  .services li::before {
    content: ""; width: 8px; height: 8px; border-radius: 50%;
    background: var(--accent); flex: none;
  }
  .tagline {
    position: absolute; left: 0; right: 0; bottom: 34px;
    text-align: center; font-size: 19px;
  }
</style>
</head>
<body>
<main class="canvas">

  <section class="card card--front" aria-label="Card front">
    <div class="front__ring" aria-hidden="true"></div>
    <div class="brand front__brand">
      <span class="brand__dot" aria-hidden="true"></span>
      <span class="brand__name">Bellcrest HVAC</span>
    </div>
    <div class="person">
      <p class="person__name">DORIAN VANCE</p>
      <p class="person__role">Owner</p>
    </div>
    <p class="contact contact--email">
      <svg width="20" height="15" viewBox="0 0 20 15" aria-hidden="true"><path d="M0 0h20v15H0z M1.5 1.5 10 8l8.5-6.5" fill-rule="evenodd"/><path d="M1 1l9 7 9-7" stroke="#2e2e30" stroke-width="1.6" fill="none"/></svg>
      dvance@bellcresthvac-example.net
    </p>
    <div class="front__rule" aria-hidden="true"></div>
    <p class="contact contact--phone">
      <svg width="16" height="16" viewBox="0 0 24 24" aria-hidden="true"><path d="M6.6 10.8a15 15 0 0 0 6.6 6.6l2.2-2.2a1 1 0 0 1 1-.25 11.4 11.4 0 0 0 3.6.57 1 1 0 0 1 1 1V20a1 1 0 0 1-1 1A17 17 0 0 1 3 4a1 1 0 0 1 1-1h3.5a1 1 0 0 1 1 1c0 1.25.2 2.45.57 3.57a1 1 0 0 1-.25 1z"/></svg>
      555-318-4702
    </p>
  </section>

  <section class="card card--back" aria-label="Card back">
    <div class="brand back__brand">
      <span class="brand__dot" aria-hidden="true"></span>
      <span class="brand__name">Bellcrest HVAC</span>
    </div>
    <div class="back__divider" aria-hidden="true"></div>
    <ul class="services">
      <li>Air Conditioning</li>
      <li>Heating</li>
      <li>Heat Pumps / Gas / Oil</li>
      <li>Ductless mini splits</li>
      <li>Controls</li>
      <li>VFD's</li>
      <li>Pumps</li>
      <li>Gas Fitting/Piping</li>
      <li>Service and New install</li>
      <li>Residential / Commercial</li>
    </ul>
    <p class="tagline">Servicing New Hampshire for 30 years</p>
  </section>

</main>
</body>
</html>
```